Copper Ridge Garage Door Sales & Repair needs a Business Card Design

I need a business card design to go with our new business logo that was created a few months ago.

Copper Ridge Garage Door specializes in selling and installing new garage doors, and new garage door openers. We also take care of all repairs to existing garage doors and garage door openers. All makes and models.

Target Market(s)

Home-owners, renters, anyone who lives in a house and has a garage. Residential and commercial garages.

Industry/Entity Type

Home Improvement

Contact Information for Business Card

I would like the business cards to have rounded corners and be double-sided. My old logo is still on my website at www.copperridgegarage.example. If I was going to incorporate a secondary color on the business cards, I think that orange is a good choice (especially since blue and orange are the colors of our Tulsa Kestrels), but I'm not opposed to seeing a different color if another color works better with my logo colors. I have two logo colors. One designed for a white background and one designed for a darker background. I'm not opposed to using both. Maybe a dark background with the white logo on one side, and a white background with the other logo color on the other side.

My business is a small, locally owned business that I am trying to grow. But I would like my business cards to look very professional. Like we have been in business for a long time. I like traditional to modern looking cards. Just something bold and memorable. My full company name is Copper Ridge Garage Door Sales & Repair. But you can just do COPPER RIDGE GARAGE DOOR, if that works better.

Font styles to use
Serif
Script

Requirements
Must have
• Rounded corners
• Double-sided
• 3-D Elements. Layering of some sort (a sketch of a garage door or a 3rd color (orange) brought in some how. I really like watermarks.
• Matte cards that you can write on.
• White on one side. (Or the lighter blue in my logo). Darker blue logo color on the other side.
• I would like our tag line on the cards somewhere... "For All Your Garage Door Needs".
• I would also like "Call For a FREE Estimate" by the phone number.
• And "Serving the Greater Metro Denver Area" somewhere on the card as well.
Nice to have
• Refer to "Business Card Details" above.

```html
<!DOCTYPE html>
<html lang="en">
<head>
<meta charset="utf-8">
<title>Copper Ridge Garage Doors – Business Card</title>
<link rel="stylesheet" href="https://fonts.googleapis.com/css2?family=Roboto:wght@400;500;700&family=Exo+2:wght@500&display=swap">
<style>
  :root {
    --navy: #414c6c;
    --navy-deep: #35405e;
    --paper: #f0f1f3;
    --white: #ffffff;
    --backdrop: #1c1c1c;
  }
  * { box-sizing: border-box; margin: 0; padding: 0; }
  html, body { width: 1200px; height: 800px; overflow: hidden; }
  body {
    background: var(--backdrop);
    font-family: "Roboto", Arial, sans-serif;
    position: relative;
  }
  .card {
    position: absolute;
    top: 238px;
    width: 535px;
    height: 306px;
    border-radius: 16px;
    overflow: hidden;
  }
  .card--front { left: 50px; background: var(--navy); color: var(--white); }
  .card--back { left: 617px; background: var(--paper); color: var(--navy); }

  .brand-name {
    position: absolute;
    font-family: "Roboto", Arial, sans-serif;
    font-weight: 700;
    text-align: center;
    line-height: 1.1;
    letter-spacing: 1px;
  }
  .card--front .brand-name { left: 26px; top: 60px; width: 160px; font-size: 22px; color: var(--white); }
  .card--back .brand-name { left: 142px; top: 82px; width: 250px; font-size: 32px; color: var(--navy); }
  .brand-name small { display: block; font-size: 0.62em; letter-spacing: 3px; margin-top: 6px; }

  .estimate {
    position: absolute; left: 25px; top: 170px;
    font-size: 21px; font-weight: 400;
  }
  .rule { position: absolute; top: 201px; height: 3px; background: var(--white); }
  .rule--left { left: 0; width: 310px; }
  .rule--right { left: 509px; width: 26px; }
  .person-name {
    position: absolute; left: 320px; top: 187px; width: 180px;
    font-family: "Exo 2", "Roboto", sans-serif; font-weight: 500;
    font-size: 21px; text-align: right; letter-spacing: 0.5px;
  }
  .person-role {
    position: absolute; right: 37px; top: 210px;
    font-size: 16px; font-weight: 500;
  }
  .contact-list { position: absolute; left: 30px; top: 214px; list-style: none; }
  .contact-list li {
    display: flex; align-items: center; height: 19.7px;
    font-size: 14.5px;
  }
  .contact-list svg { width: 11px; height: 11px; margin-right: 8px; flex: none; }

  .tagline {
    position: absolute; left: 0; width: 100%; top: 221px;
    text-align: center; font-size: 16px; font-weight: 500;
  }
  .service-band {
    position: absolute; left: 0; top: 253px; width: 100%; height: 39px;
    background: var(--navy); color: var(--white);
    display: flex; align-items: center; justify-content: center;
    font-size: 16px;
  }
</style>
</head>
<body>
  <section class="card card--front" aria-label="Card front">
    <div class="brand-name">COPPER RIDGE<small>GARAGE DOORS</small></div>
    <p class="estimate">"Call For a FREE Estimate"</p>
    <div class="rule rule--left"></div>
    <div class="rule rule--right"></div>
    <p class="person-name">Dana Whitfield</p>
    <p class="person-role">Project Manager</p>
    <ul class="contact-list">
      <li>
        <svg viewBox="0 0 12 12"><rect width="12" height="12" rx="2" fill="#fff"/><path d="M3 4.5h6v4H3z M4.5 3h3v1.5h-3z" fill="#414c6c"/></svg>
        555.014.2290
      </li>
      <li>
        <svg viewBox="0 0 12 12"><rect width="12" height="12" rx="2" fill="#fff"/><rect x="2.5" y="3.5" width="7" height="5" fill="#414c6c"/><path d="M2.5 3.5l3.5 3 3.5-3" stroke="#fff" stroke-width="0.8" fill="none"/></svg>
        dana@copperridgegarage.example
      </li>
      <li>
        <svg viewBox="0 0 12 12"><rect width="12" height="12" rx="2" fill="#fff"/><circle cx="6" cy="6" r="3.3" fill="none" stroke="#414c6c" stroke-width="1"/><path d="M2.7 6h6.6M6 2.7v6.6" stroke="#414c6c" stroke-width="0.8"/></svg>
        www.copperridgegarage.example
      </li>
      <li>
        <svg viewBox="0 0 12 12"><rect width="12" height="12" rx="2" fill="#fff"/><path d="M6 2.5a2.5 2.5 0 0 1 2.5 2.5C8.5 7 6 9.5 6 9.5S3.5 7 3.5 5A2.5 2.5 0 0 1 6 2.5z" fill="#414c6c"/><circle cx="6" cy="5" r="0.9" fill="#fff"/></svg>
        4200 Alder Park Way Suite 12, Lakeview, CO 80099
      </li>
    </ul>
  </section>

  <section class="card card--back" aria-label="Card back">
    <div class="brand-name">COPPER RIDGE<small>GARAGE DOORS</small></div>
    <p class="tagline">"For All Your Garage Door Needs"</p>
    <div class="service-band">"Serving the Greater Metro Denver Area"</div>
  </section>
</body>
</html>
```